Bref créative
Bridgewell Brochure
Brochure
The brochure I want is a double-sided, tri-fold, 8.5" x 11". I have uploaded a sketch on what I would like on each side, as well as my original brochure. I will describe what I want on each side, and each section.
Inside (refer to formatting of original brochure):
left -- I want this section to be very similar to the original, but with a new design consistent with our colors and logo. Attached is a file titled "Bridgewell Brochure -- NEW TEXT" that is the new text I want in the section.
middle -- I want the text of the original brochure to remain the same, but consistent with new design/colors, and also if we can use our logo's "cube" as the new separator between the testimonials.
right -- I want this to be all new (not like original), with the text, "Visit us on the web at: www.BridgewellHoldingsNY.example" and below that, the text, "find our Attorney tab". The designer is open to design this section any way they would like, consistent with the overall design.
Outside (refer to formatting of original brochure):
left -- this section can be just like the original brochure, just with the updated design. I still want 'scales of justice' included in this section.
middle -- same as original brochure, just with our new address: 418 Maplecrest Avenue, Floral Park, NY 11001
right -- same as original brochure, just with new design
On the whole, I am looking for a design that is a little more sleek, modern, and simple. I would urge the designers to please stay away from swirly text or design features.
Real Estate
attorneys and businessmen
I have uploaded both sides of our old brochure. We want something nearly identical, just more reflective of our colors and style.
I have also uploaded our logo, business card, and new text for the left side of the inside of the brochure.
Lastly, I am uploading a new mock-up of the 6 sections of the brochure (similar to old version).
ANY SUBMISSION THAT DEVIATES TOO MUCH FROM OUR PREVIOUS DESIGN WILL BE IMMEDIATELY ELIMINATED.

```html
<!DOCTYPE html>
<html lang="en">
<head>
<meta charset="utf-8">
<title>Bridgewell Asset Management – Tri-fold Brochure</title>
<link rel="stylesheet" href="https://fonts.googleapis.com/css2?family=Oswald:wght@500;700&family=Crimson+Text:ital,wght@0,400;0,600;1,400&display=swap">
<style>
:root{
  --navy:#1f1a5c;
  --navy-deep:#140f45;
  --gold:#d9a321;
  --gold-light:#eec45a;
  --paper:#ffffff;
  --cube-light:#f3f1ea;
  --cube-shade:#e2dfd3;
  --backdrop:#e8e7ef;
  --ink:#2b2b3a;
}
*{box-sizing:border-box;margin:0;padding:0}
html,body{width:1200px;height:901px;overflow:hidden;background:var(--backdrop)}
body{display:flex;align-items:center;justify-content:center;gap:30px;font-family:"Crimson Text",Georgia,serif}
.spread{position:relative;width:560px;height:433px;background:var(--paper);display:flex;box-shadow:0 6px 22px rgba(20,15,69,.22)}
.panel{position:relative;width:33.333%;height:100%;overflow:hidden}
.heading{font-family:"Oswald",Arial,sans-serif;text-transform:uppercase}

/* outside left */
.offering{padding:22px 14px 0}
.offering-tab{display:inline-block;background:var(--gold);color:#fff;font-size:15px;font-weight:700;padding:2px 16px 2px 8px;border-radius:0 12px 12px 0;letter-spacing:.5px}
.offer-list{list-style:none;margin-top:10px}
.offer-list li{color:var(--gold);font-size:12px;line-height:1.75}
.offer-list li::before{content:"•";color:var(--navy);margin-right:5px}
.scales{position:absolute;left:22px;top:190px;width:96px;height:90px;border-radius:6px;background:linear-gradient(180deg,#3a3578,var(--navy-deep))}
.toll{position:absolute;left:14px;top:320px;color:var(--gold);font-style:italic;font-size:12px}
.phone{position:absolute;left:14px;top:334px;color:var(--navy);font-size:22px;letter-spacing:.5px}

/* cube decoration area */
.cube-deco{position:absolute;background:linear-gradient(150deg,var(--cube-light),var(--cube-shade));opacity:.85}

/* outside middle */
.address{position:absolute;right:12px;top:18px;writing-mode:vertical-rl;color:var(--navy);font-size:8px;line-height:1.3}

/* cover */
.cover{display:flex}
.cover-band{width:20px;background:linear-gradient(180deg,var(--gold-light),var(--gold))}
.cover-edge{width:3px;background:var(--navy)}
.cover-body{flex:1;position:relative;padding:34px 10px 0}
.cover-title{color:var(--navy);font-size:25px;font-weight:700;line-height:1.02}
.brand{position:absolute;left:0;right:0;bottom:20px;text-align:center;color:var(--navy);font-family:"Oswald",Arial,sans-serif;font-weight:500;font-size:14px;line-height:1.1;text-transform:uppercase}
.brand-mark{display:block;width:20px;height:20px;margin:0 auto 4px;background:var(--gold)}

/* inside left */
.results{padding:18px 10px 0}
.bar{background:var(--navy);color:var(--gold);font-size:10px;font-weight:700;padding:3px 6px;letter-spacing:.4px}
.bar+.bar{margin-top:0}
.body-copy{color:var(--navy);font-size:8.4px;line-height:1.35;margin:6px 0 7px}
.dropcap::first-letter{float:left;font-size:26px;line-height:.9;margin-right:3px;color:var(--navy)}

/* inside middle */
.praise{padding:14px 10px 0}
.praise .bar-gold{background:var(--gold);color:var(--navy);font-size:9px;font-weight:700;padding:3px 6px;text-align:center;line-height:1.15}
.praise-lead{color:var(--navy);font-size:10px;font-weight:600;margin:6px 0 4px}
.quote{color:var(--gold);font-style:italic;font-size:8.2px;line-height:1.3}
.byline{color:var(--navy);font-size:8.2px;text-align:center;margin-top:3px;line-height:1.25}
.divider{width:14px;height:14px;background:var(--navy);margin:7px auto}

/* inside right */
.web{padding:14px 10px 0 8px}
.web-label{color:var(--gold);font-size:9px;font-weight:700;line-height:1.25}
.web-url{color:var(--gold);font-size:9.6px;font-weight:600}
.web-note{color:var(--navy);font-size:9px;font-weight:600}
.web-band{position:absolute;right:0;top:0;width:22px;height:100%;background:linear-gradient(180deg,var(--gold-light),var(--gold))}
.web .brand{right:22px}
</style>
</head>
<body>

<section class="spread spread-outside" aria-label="Brochure outside">
  <div class="panel offering">
    <span class="offering-tab heading">Offering…</span>
    <ul class="offer-list">
      <li>Prompt Professional Services</li>
      <li>Immediate Closings</li>
      <li>All Cash Purchases</li>
      <li>Decency &amp; Integrity</li>
    </ul>
    <div class="scales" role="img" aria-label="Scales of justice illustration"></div>
    <p class="toll">Toll Free</p>
    <p class="phone">1-800-555-0142</p>
  </div>

  <div class="panel mailer">
    <p class="address">Bridgewell Holdings LLC<br>418 Maplecrest Avenue, Floral Park, NY 11001</p>
    <div class="cube-deco" style="left:0;top:150px;width:150px;height:220px" role="img" aria-label="Large faint cube graphic"></div>
  </div>

  <div class="panel cover">
    <div class="cover-band"></div>
    <div class="cover-edge"></div>
    <div class="cover-body">
      <h1 class="cover-title heading">Providing<br>Solutions<br>for<br>you &amp; your<br>clients!</h1>
      <div class="cube-deco" style="left:10px;top:200px;width:120px;height:120px;opacity:.5" role="img" aria-label="Faint cube graphic"></div>
      <p class="brand"><span class="brand-mark"></span>Bridgewell<br>Asset Management</p>
    </div>
  </div>
</section>

<section class="spread spread-inside" aria-label="Brochure inside">
  <div class="panel results">
    <h2 class="bar heading">Driven by results</h2>
    <p class="body-copy dropcap">Bridgewell Asset Management has established itself as a premier investment corporation specializing in the purchase of properties in distressed conditions or facing foreclosure.</p>
    <p class="body-copy">We recognize this is a delicate situation where attorneys need fast, reliable answers. With extensive experience in real estate, financing, sales and development, we are here to offer workable solutions for professionals and their clients.</p>
    <h2 class="bar heading">When a consolidation is needed</h2>
    <p class="body-copy dropcap">Bridgewell Asset Management can close quickly, with all cash and no mortgage contingencies. Reliability is one of our core values.</p>
    <p class="body-copy">Bridgewell Asset Management looks forward to the opportunity to provide outstanding service to you and your clients.</p>
  </div>

  <div class="panel praise">
    <h2 class="bar-gold heading">Don't just take our word for it</h2>
    <p class="praise-lead">Hear what your colleagues have to say!</p>
    <p class="quote">“I have had the pleasure of dealing with the principals on numerous occasions. Each closing was handled quickly and with care.”</p>
    <p class="byline">Karen L. Hollis<br>Attorney at Law</p>
    <div class="divider"></div>
    <p class="quote">“I have been very satisfied with the results for my clients. They made a hard situation simple and kept every promise.”</p>
    <p class="byline">Marcus Delane<br>Attorney at Law</p>
    <div class="divider"></div>
    <p class="quote">“Bridgewell is diligent and professional. Their offers are fair and their team is a pleasure to work with.”</p>
    <p class="byline">Priya Wend<br>Attorney at Law</p>
  </div>

  <div class="panel web">
    <p class="web-label heading">Visit us on the web at:</p>
    <p class="web-url">www.BridgewellHoldingsNY.example</p>
    <p class="web-note">(find our Attorney tab)</p>
    <div class="cube-deco" style="left:0;top:150px;width:140px;height:190px" role="img" aria-label="Large faint cube graphic"></div>
    <div class="web-band"></div>
    <p class="brand"><span class="brand-mark"></span>Bridgewell<br>Asset Management</p>
  </div>
</section>

</body>
</html>
```